Cruise price comparison web design project

The project's name is Wellenfuchsportal.
www.wellenfuchsportal.de
The current design (which I don't really like) can be found here:
http://wfp02.wellenfuchsportal.de/

I m not too happy with what the current developers have been done so far (in terms of design), so I hope to find a great designer her to develop a design that kicks arses. : )

We are currently developing a site for the German market that brings travel agents and cruise holiday makers together. We are not an ordinary travel agency.
Wellenfuchsportal is a quick and convenient way to have independent travel agencies compete to offer our site visitors the best cruise deal available in Europe.

Here is a short video that explains what one of our competitors does; it gives a good overview as our site will be similar:
http://www.voyabidder.com/video_how_voyabidder_works.php
(Voyabidder.com is not a great website in terms of design, so please dont get me wrong.)

The logo has already been created, but both the colours (should remain blueish) and the font can be modified. The font colour can be changed dramatically if you think this is of advantage.

The Website design should be professional and unique and become an eye catcher. It must attract visitors of all age groups, a "wow-effect" is definitely a bonus.
Users should easily see what this website is about.

We need the following text on our homepage:

"Immer der beste Preis -
denn Reisebüros kämpfen um Sie!"
(means "Always the best rate - as travel agents compete offer the best deal")
This is a sort of headline.

We also need:

So funktioniert Wellenfuchsportal:
1. Wunschkreuzfahrt wählen
2. Angebote erhalten und vergleichen
3. Reisebüro kontaktieren und buchen

(This explains briefly how our system works.)

Aside banners maybe needed later for advertising.

Additions I need on the front page are:
- Login / Sign-Up / Your benefits
(I quite like the way it's done on http://www.lirmatimes.com, at the very top of the page)
- Recommendation-link
(for everything else: Pls. refer to wfp02.wellenfuchsportal.de
- 3 or 4 "top offers of the week"
(current format is not very appealing; offers can be displayed as on http://sailings.tripnuvo.com/affiliate/promo.rvlx?OfferID=DOLUMA27 or

A maritime look is surely an option here, as we focus on cruises. But maybe you can surprise me with a great idea.

I quite like the designs where basically one photo / picture is used.
Some examples which look great IMHO:
http://pell-works.artfolioz.com/art/Glint-Swimmers-519304826
http://quorvanwebdesign.artfolioz.com/art/Website-Design-736152940
The following designer has also done a great job:
http://pixelmaker4387.artfolioz.com/gallery/

ATTACHED:
- logo
- Glint-Swimmers Design .png
- Flyer we use to attract travel agencies
- photo we use for the flyer (we own the rights)

Please get in touch with me if there are any questions or if you require further details. I ll get back to all inquiries / messages as soon as possible, usually within a few hours... Feel free to ask technical questions, too, (if any), the developer will be of assistance.

Reason: I decided to extend the deadline to have more time to comment on your designs and allow you to submit a few more proposals.

Reason: Sorry, more time needed to comment on all designs. Apart from this, some designers asked for more time.

Dear All,

Thank you so much for all your proposals.
Later today I will have a decent internet connection connection again, so I will be able to finally comment on your ideas and visions.

Hopefully next week we can finalize this project. Feel free to submit more designs or ask any questions if there are any.
Remember: Wellenfuchsportal won't be an ordinary travel agent. It brings cruise holiday makers and travel agents together.

Best

Target Market(s)

Holidaymakers / potential cruise holiday makers between 20 and 80.

Industry/Entity Type

Advertising

Requirements
Should not have
• Design should not use old-style, serif fonts.

```html
<!DOCTYPE html>
<html lang="de">
<head>
<meta charset="utf-8">
<title>Wellenfuchsportal – Kreuzfahrt-Schnäppchen</title>
<link rel="stylesheet" href="https://fonts.googleapis.com/css2?family=Tinos&family=Arimo:wght@400;700&family=Roboto+Condensed:wght@400&family=Ubuntu:wght@500;700&display=swap">
<style>
:root{
  --brand:#1f5aa6;
  --brand-dark:#123f86;
  --link:#1b52a8;
  --ink:#111;
  --white:#fff;
  --sky:#cddbe6;
  --sea:#1d4c86;
  --sea-deep:#12376a;
  --deck:#7a5a3e;
  --shadow:rgba(0,0,0,.55);
}
*{margin:0;padding:0;box-sizing:border-box}
html,body{width:1200px;height:900px;overflow:hidden;background:var(--white)}
.page{position:relative;width:1200px;height:900px;overflow:hidden;font-family:"Arimo",Arial,sans-serif;color:var(--ink)}
.abs{position:absolute}

/* header */
.brand-mark{left:18px;top:32px;display:flex;align-items:center;gap:8px}
.brand-mark .dot{width:74px;height:74px;border-radius:50%;background:var(--brand)}
.site-title{left:0;width:1260px;top:24px;text-align:center;font:52px "Tinos",serif;color:var(--brand-dark);letter-spacing:1px}
.tagline{left:282px;top:92px;font:700 22px "Arimo",sans-serif;color:var(--brand)}
.hotline{right:12px;top:32px;text-align:right;color:var(--brand);font-size:14px}
.hotline strong{display:block;font-weight:400;font-size:18px;margin-top:10px}
.account{right:12px;top:99px;font:700 17px "Arimo",sans-serif;color:var(--brand);display:flex;gap:24px}

/* hero */
.hero{left:0;top:140px;width:1200px;height:585px;
  background:linear-gradient(180deg,var(--sky) 0%,#8fb0cd 12%,#2f64a0 20%,var(--sea) 40%,var(--sea-deep) 60%,#3b5a7a 72%,#a78a68 82%,var(--deck) 100%)}
.hero-mask{left:0;top:0}
.nav{left:252px;top:172px;display:flex;gap:16px;font:20px "Roboto Condensed",sans-serif;color:var(--brand);white-space:nowrap}
.hero-head{left:0;width:1200px;text-align:center;color:var(--white);font-family:"Ubuntu",sans-serif;font-weight:700;text-shadow:2px 2px 3px var(--shadow)}
.hero-head.h1{top:230px;font-size:27px;letter-spacing:1px}
.hero-head.h2{top:270px;font-size:22px;font-weight:500}

.offer{color:var(--white);font:500 15px/1.45 "Ubuntu",sans-serif;text-shadow:1px 1px 2px var(--shadow)}
.offer h3{font-size:18px;font-weight:500}
.offer .price{font-size:15px}
.order-btn{background:var(--white);color:var(--link);font:15px "Arimo",sans-serif;padding:2px 6px;box-shadow:1px 1px 3px rgba(0,0,0,.4)}

.ship-thumb{border:2px solid #9cc3e0;border-radius:10px;overflow:hidden;box-shadow:0 0 6px rgba(255,255,255,.6)}
.ship-thumb .caption{position:absolute;left:0;right:0;bottom:8px;text-align:center;color:var(--white);font:14px "Arimo",sans-serif;text-shadow:1px 1px 2px #000}

.how{right:12px;top:345px;text-align:right;color:var(--white);font-family:"Ubuntu",sans-serif;text-shadow:1px 1px 2px var(--shadow)}
.how h2{font-size:21px;font-weight:700;margin-bottom:38px}
.how li{list-style:none;font-size:15px;font-weight:500;margin-bottom:12px}

.promo-box{right:0;top:644px;width:245px;height:72px;background:rgba(255,255,255,.92);text-align:right;padding:6px 10px 0 0;font-size:15px;line-height:1.3}
.promo-box b{color:var(--brand-dark)}

/* footer */
.footer-col{top:733px;font-size:13px;line-height:17px;color:var(--link)}
.footer-col li{list-style:none}
.about{left:17px;top:840px;width:1160px;font-size:12px;line-height:15px}
.stamp{top:870px;font-size:12px}
</style>
</head>
<body>
<div class="page">

  <div class="hero abs" role="img" aria-label="Foto: Blick vom Bug eines Kreuzfahrtschiffs mit Holzdeck auf das tiefblaue Meer, links ein weißes Schiff am Horizont"></div>

  <svg class="hero-mask abs" width="1200" height="900" viewBox="0 0 1200 900" aria-hidden="true">
    <path d="M0 0H1200V142C900 140 500 142 300 150C255 152 240 170 225 200C215 220 205 226 180 228H0Z" fill="#fff"/>
    <path d="M0 718H1200V900H0Z" fill="#fff"/>
  </svg>

  <div class="brand-mark abs"><span class="dot"></span></div>
  <div class="site-title abs">WELLENFUCHSPORTAL</div>
  <div class="tagline abs">Immer Der Beste Preis - Denn Reise Buros Kampfen Um Sie!</div>
  <div class="hotline abs">Mit Kreuzfahrt-Experten Sprechen<strong>04821-639207</strong></div>
  <nav class="account abs"><span>Log In</span><span>Sign Up</span></nav>

  <nav class="nav abs">
    <span>So Gehts</span><span>Angebote Erhalten</span><span>Kreuzfahrtsuche</span><span>Reedereien Und Schiffe</span><span>Specials</span><span>Kontakt</span><span>Fehlermeldung</span><span>Trac</span>
  </nav>

  <div class="hero-head h1 abs">Finden Sie Ihr Kreuzfahrt - Scnappchen!</div>
  <div class="hero-head h2 abs">Hier finden Sie wochenaktuell eine Auswahl der attraktivsten Kreuzfahrt - Angebote</div>

  <div class="ship-thumb abs" style="left:17px;top:348px;width:182px;height:147px;background:linear-gradient(180deg,#c9b7b2 0%,#b9c6d6 50%,#4a6f96 100%)" role="img" aria-label="Foto: Kreuzfahrtschiff Aurora of the Waves auf See"><div class="caption">Aurora of the Waves</div></div>

  <div class="offer abs" style="left:256px;top:345px;width:340px">
    <h3>Von der Stadt des Tangos zum Big Apple</h3>
    <div style="text-align:right;margin-top:6px">Inkl. Flugen mit Falkenwind Air, Transfers &amp;<br>Hotelubernachtung in Buenos Aires<br>22 Tage Sudamerika Kreuzfahrt<br>Termin Juli 2012</div>
    <div class="price" style="margin-top:-2px">ab Euro 2.899<br>Pro Person</div>
  </div>
  <span class="order-btn abs" style="left:449px;top:473px">Angebot Bestellen</span>

  <div class="offer abs" style="left:17px;top:550px;width:300px;line-height:1.55">
    <h3>Rund um Island - ab/bis Hamburg</h3>
    <div style="margin-top:6px">Top - Angebot</div>
    <div style="margin-top:6px">12 Tage Island Kreuzfahrt<br>Termin 26. Juni 2012</div>
    <div style="margin-top:6px">ab Euro 1.300<br>Pro Person</div>
  </div>
  <span class="order-btn abs" style="left:151px;top:673px">Angebot Bestellen</span>

  <div class="ship-thumb abs" style="left:415px;top:551px;width:182px;height:145px;background:linear-gradient(180deg,#5a6f86 0%,#8aa3b8 45%,#8b6c4c 100%)" role="img" aria-label="Foto: Promenadendeck der Serenade Horizon mit Holzboden"><div class="caption">Serenade Horizon</div></div>

  <div class="how abs">
    <h2>So Funktioniert Wellenfuchsportal:</h2>
    <ol>
      <li>1. Wunschkreuzfahrt Wahlen</li>
      <li>2. Angebote Erhalten Und Vergleichen</li>
      <li>3. Reiseburo Kontaktieren Und Buchen</li>
    </ol>
  </div>

  <div class="promo-box abs">Angebote und Gesuche<br>Kostenlos einstellen - jetzt<br><b>anmelden</b> oder neu <b>registrieren</b></div>

  <ul class="footer-col abs" style="left:17px"><li>Uber uns</li><li>Uber Wellenfuchsportal.de</li><li>Jobs</li><li>Partner</li><li>Werbung auf Wellenfuchsportal.de</li></ul>
  <ul class="footer-col abs" style="left:343px"><li>Presse</li><li>Pressematerial</li><li>Wellenfuchsportal.de in den Medien</li><li>Pressemitteilungen</li><li>Wellenfuchsportal und die Sozialen Medien</li></ul>
  <ul class="footer-col abs" style="left:724px;top:735px"><li>Hilfe &amp; Service</li><li>Kundenmeinungen</li><li>Kontakt</li><li>FAQ's</li></ul>
  <ul class="footer-col abs" style="left:952px"><li>Rechtiches</li><li>Disclaimer / Haftungsausschluss</li><li>Nutzungsbedingungen</li><li>Impressum</li></ul>

  <p class="about abs">Wellenfuchsportal.de ist ein vollig neuer Service, welcher Sie schnell und bequem den gunstigsten Preis fur eiene Kreuzfahrt finden lasst. Lange Suchen nach preiswerten Kreuzfahrten gehoren ab sofort der Vergangenheit an, denn Reiseburos kampfen um Sie. Sparen Sie bares Geld und testen Sie Wellenfuchsportal.de - naturlich vollig kostenlos. Finden Sie Ihr Kreuzfahrt - Schnappchen!</p>
  <div class="stamp abs" style="left:17px">Zuletzt aktualisiert: 05.12.2012</div>
  <div class="stamp abs" style="right:14px">C 2010-2012 Wellenfuchsportal.de</div>

</div>
</body>
</html>
```